Web design for boutique law firm

Web design for law firm; practice areas include:
-international intellectual property counseling
-general corporate (contract negotiation, licensing, distribution agreements
-see my *very* outdated website at www.pvtlegalhouse.com: here is some of the home page content:

"PVT Law Group enjoys providing proactive, business-minded, efficient legal solutions for individuals and companies that benefit from major law firm experience at reasonable rates.

Some areas of emphasis include:

Counseling individuals and companies with respect to clearing, selecting, securing, managing, commercializing, and protecting intellectual property assets around the world. This includes traditional global brand management, marketing, advertising, and enforcement work as well as litigation.
PVT Law Group also provides general counseling services for individuals and businesses, from start-up advice to sophisticated business transactions strategy, agreement negotiating, dispute resolution, and litigation.
Before founding PVT Law Group in 2008, Curtis L. Abernathy led the Trademark, Copyright, & Brand Management Group for Falkner & Ingleby's Seattle office. Curtis was also a senior associate at Silicon Valley based Hartwell, Bexley, Oduya, & Penrose."

Target Market(s)

Clients/potential clients needing tier one, international intellectual property advice with "mega" law firm experience for much less than what we were/would be charging at the "mega firms".

Industry/Entity Type

Legal

Number of Pages Required

4 page

Font styles to use
Serif
Sans Serif

Colors

Designer to choose colors to be used in the design.

Requirements
Must have
• +Improvement over everything on current site at www.pvtlegalhouse.com.
• +Pictures/bios for me and my team (four of us right now).
• +Easy to update and add/remove content.
• +Must be superior in design (look, feel, ease of use, classy and elegant, but hip, reflects international practice).
• +i have logos and color schemes (see current website) but will consider improvements.
Nice to have
• Let me know your thoughts.
Should not have
• No cheese; no overt sales pitches or marketing (since law firm).

```html
<!DOCTYPE html>
<html lang="en">
<head>
<meta charset="utf-8">
<title>PVT Law Group PLLC</title>
<link href="https://fonts.googleapis.com/css2?family=Roboto:wght@300;400;500;700&family=Roboto+Condensed:wght@400;700&family=Raleway:wght@400;500&display=swap" rel="stylesheet">
<style>
:root{
  --orange:#f26a21;
  --black:#111;
  --ink:#222;
  --grey:#666;
  --light:#f1f1f1;
  --white:#fff;
  --brown-1:#3a2a20;
  --brown-2:#6a4a35;
}
*{box-sizing:border-box;margin:0;padding:0}
html,body{width:1200px;height:3072px;overflow:hidden;background:var(--white);font-family:'Roboto',sans-serif;color:var(--ink)}
.page{position:relative;width:1200px;height:3072px}
.abs{position:absolute}

/* header */
.topbar{left:728px;top:0;width:472px;height:32px;background:#e6e6e6;border-bottom-left-radius:16px}
.topbar .phone{left:28px;top:4px;color:var(--orange);font:700 19px 'Roboto Condensed',sans-serif;display:flex;align-items:center;gap:8px}
.dot-ico{width:22px;height:22px;border-radius:50%;background:var(--orange);display:inline-block}
.social{display:flex;gap:5px}
.social span{width:24px;height:24px;border-radius:50%;background:var(--black);display:block}
.topbar .social{position:absolute;left:185px;top:4px}
.brand{left:168px;top:56px;display:flex;align-items:center;gap:12px;font:400 24px 'Roboto',sans-serif;color:var(--ink)}
.brand i{width:26px;height:26px;background:var(--orange);display:block}
.consult{left:732px;top:56px;width:306px;height:40px;border:1px solid #ddd;display:flex;align-items:center;font:400 18px 'Raleway',sans-serif;color:var(--ink)}
.consult i{width:44px;height:38px;background:var(--orange);margin-right:14px;display:block}
.nav{left:0;top:115px;width:1200px;height:43px;background:var(--black);display:flex;padding-left:162px}
.nav a{color:#ddd;text-decoration:none;font:400 15px 'Roboto',sans-serif;line-height:43px;text-align:center}
.nav a.active{background:var(--orange);color:var(--white)}

/* hero */
.hero{left:0;top:158px;width:1200px;height:502px;background:linear-gradient(135deg,#6d6e70,#3d3e41 55%,#2a2b2e)}
.hero-caption{left:0;top:585px;width:1200px;height:75px;background:rgba(0,0,0,.65)}
.hero-caption p{position:absolute;left:164px;top:8px;color:var(--white);font:500 22px/29px 'Roboto Condensed',sans-serif}
.call-btn{left:850px;top:600px;width:186px;height:42px;border:2px solid var(--white);background:var(--orange);color:var(--white);font:500 22px 'Roboto Condensed',sans-serif;display:flex;align-items:center;justify-content:center;gap:8px}
.call-btn i{width:20px;height:20px;border-radius:50%;background:var(--white);display:block}
.slide-arrow{top:386px;width:24px;height:28px;background:#222;color:#fff;font:700 16px sans-serif;text-align:center;line-height:28px}

/* welcome */
.welcome-title{left:0;top:702px;width:1200px;text-align:center;font:400 35px 'Raleway',sans-serif;color:var(--ink)}
.welcome-title b{color:var(--orange);font-weight:400}
.welcome-text{left:175px;top:772px;width:850px;text-align:center;font:400 10.5px/19px 'Roboto',sans-serif;color:#444}
.read-more{left:0;top:893px;width:1200px;text-align:center;font:400 13px 'Roboto',sans-serif;color:var(--orange);text-decoration:underline}

/* services hex */
.hex-svg{left:0;top:940px}
.hex-label{font:500 17px 'Roboto Condensed',sans-serif;fill:#fff}

/* why */
.why{left:0;top:1438px;width:1200px;height:524px;background:linear-gradient(180deg,var(--brown-2),var(--brown-1) 60%,#2a1e17)}
.why-title{left:0;top:1470px;width:1200px;text-align:center;font:400 35px 'Raleway',sans-serif;color:var(--white)}
.feature{width:260px;color:#fff}
.feature h4{font:400 16px 'Roboto',sans-serif;margin-bottom:4px}
.feature p{font:400 11px/16px 'Roboto',sans-serif;color:#ddd}
.feature.left{text-align:right}

/* team */
.team{left:0;top:1962px;width:1200px;height:414px;background:var(--light)}
.section-title{left:0;width:1200px;text-align:center;font:400 35px 'Raleway',sans-serif;color:var(--ink)}
.card{top:2093px;width:201px;height:248px;background:var(--white);box-shadow:0 2px 6px rgba(0,0,0,.15)}
.card .photo{width:201px;height:150px;background:linear-gradient(180deg,#d7d7d7,#b8b8b8)}
.card .name{position:absolute;top:170px;width:100%;text-align:center;font:400 14px 'Roboto',sans-serif}
.card .mail{position:absolute;top:206px;width:100%;text-align:center;font:400 12px 'Roboto',sans-serif;color:#555}
.card .tab{position:absolute;right:14px;bottom:0;width:36px;height:16px;border-radius:18px 18px 0 0;background:#999}
.card.featured{background:var(--black)}
.card.featured .name,.card.featured .mail{color:#fff}
.card.featured .mail{font-weight:500}
.card .badge{position:absolute;left:86px;top:132px;width:30px;height:30px;border-radius:50%;background:var(--orange)}
.side-arrow{font:300 48px 'Roboto',sans-serif;color:#ccc}

/* testimonials */
.quote{left:230px;top:2488px;width:740px;text-align:center;font:italic 400 14px/26px 'Roboto',sans-serif;color:#333}
.quote-mark{font:700 50px Georgia,serif;color:#ccc}
.quote-name{left:0;top:2585px;width:1200px;text-align:center;font:400 15px 'Roboto',sans-serif;color:#444}
.dots{left:574px;top:2622px;display:flex;gap:6px}
.dots span{width:8px;height:8px;border-radius:50%;background:#aaa}
.dots span:first-child{background:var(--orange)}

/* newsletter */
.newsletter{left:0;top:2673px;width:1200px;height:71px;background:var(--orange)}
.newsletter h3{position:absolute;left:248px;top:20px;color:var(--black);font:400 25px 'Raleway',sans-serif}
.env{left:164px;top:2692px}
.nl-input{left:662px;top:2694px;width:254px;height:30px;background:#fff;font:400 11px 'Roboto',sans-serif;padding:9px 10px;color:#333}
.nl-btn{left:916px;top:2694px;width:122px;height:30px;background:var(--black);color:#fff;font:500 16px 'Roboto Condensed',sans-serif;text-align:center;line-height:30px}

/* footer */
.footer{left:0;top:2744px;width:1200px;height:283px;background:#141414}
.foot-h{top:2784px;color:#fff;font:400 16px 'Roboto',sans-serif}
.foot-rule{top:2808px;width:30px;height:2px;background:var(--orange)}
.quick-links{left:164px;top:2824px;list-style:none}
.quick-links li{color:#bbb;font:400 12px/28px 'Roboto',sans-serif}
.quick-links li::before{content:"› ";color:var(--orange)}
.contact-list{left:326px;top:2830px;list-style:none}
.contact-list li{display:flex;gap:12px;color:#ccc;font:400 13px/18px 'Roboto',sans-serif;margin-bottom:22px}
.contact-list i{width:18px;height:18px;border-radius:50%;background:var(--orange);flex:none}
.field{left:592px;width:208px;height:30px;background:#fff;border-radius:3px;font:400 11px 'Roboto',sans-serif;padding:8px 10px;color:#333}
.submit{left:592px;top:2970px;width:98px;height:30px;background:var(--orange);color:#fff;font:400 16px 'Roboto',sans-serif;padding:5px 10px}
.foot-social{left:852px;top:2840px}
.foot-social span{background:var(--orange)}
.foot-brand{left:852px;top:2900px;color:var(--orange);font:400 18px 'Roboto',sans-serif;white-space:nowrap}
.copyright{left:0;top:3027px;width:1200px;height:45px;background:var(--orange);text-align:center;font:400 13px/45px 'Roboto',sans-serif;color:var(--black)}
</style>
</head>
<body>
<div class="page">

  <!-- header -->
  <div class="abs topbar">
    <div class="abs phone"><span class="dot-ico"></span>206.555.0148</div>
    <div class="social"><span></span><span></span><span></span><span></span></div>
  </div>
  <div class="abs brand"><i></i>PVT Law Group PLLC</div>
  <div class="abs consult"><i></i>Request A Free Consultation</div>
  <nav class="abs nav">
    <a class="active" style="width:94px">Home</a>
    <a style="width:120px">About Us</a>
    <a style="width:166px">Our Services</a>
    <a style="width:172px">Our Experience</a>
    <a style="width:130px">Our Team</a>
    <a style="width:140px">Contact Us</a>
  </nav>

  <!-- hero -->
  <div class="abs hero" role="img" aria-label="Overhead photo of business people at a table assembling puzzle pieces labelled Advice, Direction, Focus and Results"></div>
  <div class="abs slide-arrow" style="left:6px">‹</div>
  <div class="abs slide-arrow" style="left:1164px">›</div>
  <div class="abs hero-caption"><p>We Provide  Efficient Legal Solutions For Individuals &amp; Companies That<br>Benefit From Major Law Firm Experience At Reasonable Rates</p></div>
  <div class="abs call-btn"><i></i>Call Us Today</div>

  <!-- welcome -->
  <h1 class="abs welcome-title">Welcome To <b>PVT</b> LAW GROUP PLLC</h1>
  <div class="abs welcome-text">
    <p>PVT Law Group enjoys providing proactive, business-minded, efficient legal solutions for individuals &amp; companies that benefit from major law firm experience at reasonable rates. Some areas of emphasis include:</p>
    <p>Counseling individuals and companies with respect to clearing, selecting, securing, managing, commercializing, and protecting intellectual property assets around the world. This includes traditional global brand management, marketing, advertising, and enforcement work as well as litigation.</p>
    <p>PVT Law Group also provides general counseling services for individuals and businesses, from start-up advice to sophisticated business transactions strategy, agreement negotiating, dispute resolution, and litigation.</p>
  </div>
  <div class="abs read-more">Read More</div>

  <!-- services -->
  <svg class="abs hex-svg" width="1200" height="470" viewBox="0 940 1200 470">
    <defs>
      <linearGradient id="hexPhoto" x1="0" y1="0" x2="0" y2="1">
        <stop offset="0" stop-color="#b9aa98"/><stop offset="1" stop-color="#4b3f35"/>
      </linearGradient>
    </defs>
    <g stroke="#e4e4e4" stroke-width="8">
      <polygon role="img" aria-label="Photo of hands sheltering a house" points="378,952 481,1011 481,1129 378,1188 276,1129 276,1011" fill="url(#hexPhoto)"/>
      <polygon points="604,952 707,1011 707,1129 604,1188 502,1129 502,1011" fill="#111"/>
      <polygon role="img" aria-label="Photo of a business handshake" points="824,952 926,1011 926,1129 824,1188 721,1129 721,1011" fill="url(#hexPhoto)"/>
      <polygon role="img" aria-label="Photo of colleagues reviewing documents" points="262,1151 365,1210 365,1330 262,1389 160,1330 160,1210" fill="url(#hexPhoto)"/>
      <polygon role="img" aria-label="Photo of a hand signing an agreement" points="488,1151 590,1210 590,1330 488,1389 385,1330 385,1210" fill="url(#hexPhoto)"/>
      <polygon role="img" aria-label="Photo of a client consultation" points="712,1151 815,1210 815,1330 712,1389 610,1330 610,1210" fill="url(#hexPhoto)"/>
      <polygon role="img" aria-label="Photo of a counseling meeting" points="934,1151 1036,1210 1036,1330 934,1389 831,1330 831,1210" fill="url(#hexPhoto)"/>
    </g>
    <text x="604" y="1040" text-anchor="middle" fill="#555" font-family="Roboto,sans-serif" font-size="14">PVT Law Group PLLC</text>
    <text x="604" y="1095" text-anchor="middle" fill="#fff" font-family="Raleway,sans-serif" font-size="32">Our</text>
    <text x="604" y="1131" text-anchor="middle" fill="#fff" font-family="Raleway,sans-serif" font-size="32">Services</text>
    <g class="hex-label" text-anchor="middle">
      <text x="378" y="1101">International</text><text x="378" y="1121">Intellectual Property</text><text x="378" y="1141">Counseling</text>
      <text x="824" y="1121">Contract</text><text x="824" y="1141">Negotiation</text>
      <text x="262" y="1325">Licensing</text><text x="262" y="1345">Service</text>
      <text x="488" y="1317">Distribution</text><text x="488" y="1337">Agreements</text>
      <text x="712" y="1320">Counseling</text><text x="712" y="1340">Individuals</text>
      <text x="934" y="1315">General</text><text x="934" y="1335">Counseling</text>
    </g>
  </svg>

  <!-- why choose us -->
  <div class="abs why" role="img" aria-label="Photo of an empty wood-panelled courtroom"></div>
  <h2 class="abs why-title">Why Choose Us</h2>
  <div class="abs" style="left:570px;top:1526px;width:60px;height:3px;background:var(--orange)"></div>
  <svg class="abs" style="left:0;top:1438px" width="1200" height="524" viewBox="0 1438 1200 524">
    <circle cx="600" cy="1730" r="123" fill="none" stroke="#fff" stroke-width="2"/>
    <circle cx="600" cy="1730" r="82" fill="#fff"/>
    <text x="600" y="1724" text-anchor="middle" fill="#222" font-family="Roboto,sans-serif" font-size="16">PVT Law Group</text>
    <text x="600" y="1746" text-anchor="middle" fill="#222" font-family="Roboto,sans-serif" font-size="16">PLLC</text>
    <g fill="#fff">
      <circle cx="500" cy="1622" r="5"/><circle cx="480" cy="1730" r="5"/><circle cx="500" cy="1838" r="5"/>
      <circle cx="700" cy="1622" r="5"/><circle cx="720" cy="1730" r="5"/><circle cx="700" cy="1838" r="5"/>
    </g>
    <g fill="#f26a21" stroke="#fff" stroke-width="4">
      <circle cx="438" cy="1608" r="42"/><circle cx="401" cy="1730" r="42"/><circle cx="438" cy="1843" r="42"/>
      <circle cx="762" cy="1608" r="42"/><circle cx="799" cy="1730" r="42"/><circle cx="762" cy="1843" r="42"/>
    </g>
    <g fill="none" stroke="#fff" stroke-width="3" stroke-linecap="round">
      <path d="M426 1596c0 14 10 24 24 24l4-7-7-5-4 4c-4-2-7-5-9-9l4-4-5-7z" fill="#fff" stroke="none"/>
      <circle cx="401" cy="1730" r="10"/><circle cx="401" cy="1730" r="3" fill="#fff"/>
      <path d="M438 1830a10 10 0 0 1 6 18v5h-12v-5a10 10 0 0 1 6-18z"/>
      <circle cx="762" cy="1600" r="9"/><path d="M746 1625c4-8 28-8 32 0"/>
      <rect x="785" y="1718" width="28" height="24" rx="2"/><path d="M785 1726h28"/>
      <circle cx="762" cy="1836" r="7"/><path d="M748 1858c3-10 25-10 28 0"/>
    </g>
  </svg>
  <div class="abs feature left" style="left:128px;top:1570px"><h4>Unbiased Recommendations</h4><p>Clear advice shaped around your goals<br>[+]...read more here</p></div>
  <div class="abs feature left" style="left:90px;top:1697px"><h4>Proactive Service</h4><p>Issues spotted early and handled<br>[+]...read more here</p></div>
  <div class="abs feature left" style="left:126px;top:1810px"><h4>Superior Advice</h4><p>Guidance from major firm veterans<br>[+]...read more here</p></div>
  <div class="abs feature" style="left:813px;top:1570px"><h4>Expert Guidance</h4><p>Global know-how on brand matters<br>at fair rates...[+]</p></div>
  <div class="abs feature" style="left:845px;top:1697px"><h4>Business-Minded Solution</h4><p>Practical counsel for your company<br>and its growth...[+]</p></div>
  <div class="abs feature" style="left:813px;top:1810px"><h4>Efficient Legal Solutions</h4><p>Focused work that respects budgets<br>and timelines...[+]</p></div>

  <!-- team -->
  <div class="abs team"></div>
  <h2 class="abs section-title" style="top:1998px">Our Team</h2>
  <div class="abs" style="left:570px;top:2052px;width:60px;height:3px;background:var(--orange)"></div>
  <div class="abs side-arrow" style="left:110px;top:2180px">‹</div>
  <div class="abs side-arrow" style="left:1055px;top:2180px">›</div>
  <div class="abs card featured" style="left:158px">
    <div class="photo" role="img" aria-label="Portrait photo of Curtis L. Abernathy" style="background:linear-gradient(180deg,#8a8a8a,#3a3a3a)"></div>
    <span class="badge"></span>
    <div class="name">Curtis L. Abernathy</div>
    <div class="mail">curtis@pvtlegalhouse.com</div>
  </div>
  <div class="abs card" style="left:383px">
    <div class="photo" role="img" aria-label="Portrait photo of Marcus Ellery"></div>
    <div class="name">Marcus Ellery</div><div class="mail">inquiry@pvtlegalhouse.com</div><span class="tab"></span>
  </div>
  <div class="abs card" style="left:608px">
    <div class="photo" role="img" aria-label="Portrait photo of Jenny Halvorsen"></div>
    <div class="name">Jenny Halvorsen</div><div class="mail">inquiry@pvtlegalhouse.com</div><span class="tab"></span>
  </div>
  <div class="abs card" style="left:831px">
    <div class="photo" role="img" aria-label="Portrait photo of Dana Whitlock"></div>
    <div class="name">Dana Whitlock</div><div class="mail">inquiry@pvtlegalhouse.com</div><span class="tab"></span>
  </div>

  <!-- testimonials -->
  <h2 class="abs section-title" style="top:2412px">Clients Testimonials</h2>
  <div class="abs side-arrow" style="left:130px;top:2490px">‹</div>
  <div class="abs side-arrow" style="left:1036px;top:2490px">›</div>
  <div class="abs quote-mark" style="left:190px;top:2470px">“</div>
  <div class="abs quote">Lorem ipsum dolor sit amet, consectetuer adipiscing elit, sed diam nonummy nibh euismod tincidunt ut laoreet dolore magna aliquam erat volutpat. Ut wisi enim ad minim veniam, quis nostrud exercitation ullamcorper suscipit lobortis nisl ut aliquip ex ea commodo consequat.</div>
  <div class="abs quote-mark" style="left:766px;top:2538px">”</div>
  <div class="abs quote-name">Curtis L. Abernathy</div>
  <div class="abs dots"><span></span><span></span><span></span><span></span></div>

  <!-- newsletter -->
  <div class="abs newsletter"><h3>Subscribe Our Newsletter</h3></div>
  <svg class="abs env" width="76" height="34" viewBox="0 0 76 34">
    <g fill="none" stroke="#111" stroke-width="3">
      <rect x="22" y="4" width="50" height="26"/><path d="M22 4l25 16 25-16"/>
      <path d="M2 12h14M6 19h10M10 26h6"/>
    </g>
  </svg>
  <svg class="abs" style="left:568px;top:2690px" width="80" height="30" viewBox="0 0 80 30"><path d="M2 22c20-14 44-14 70-8m-10-6 10 6-10 6" fill="none" stroke="#111" stroke-width="2"/></svg>
  <div class="abs nl-input">Enter Your Email Address</div>
  <div class="abs nl-btn">SUBSCRIBE</div>

  <!-- footer -->
  <div class="abs footer"></div>
  <div class="abs foot-h" style="left:164px">Quick Links</div>
  <div class="abs foot-rule" style="left:164px"></div>
  <ul class="abs quick-links"><li>Home</li><li>About Us</li><li>Our Services</li><li>Our Experience</li><li>Our Team</li><li>Contact Us</li></ul>

  <div class="abs foot-h" style="left:326px">Contact Details</div>
  <div class="abs foot-rule" style="left:326px"></div>
  <ul class="abs contact-list">
    <li><i></i><span>PVT Law Group PLLC<br>742 Alder Ave, Suite 4,<br>Seattle WA 98109</span></li>
    <li><i></i><span>206.555.0148</span></li>
    <li><i></i><span>206.555.0149</span></li>
    <li><i></i><span>curtis@pvtlegalhouse.com</span></li>
  </ul>

  <div class="abs foot-h" style="left:592px">Quick Inquiry</div>
  <div class="abs foot-rule" style="left:592px"></div>
  <div class="abs field" style="top:2830px">Name</div>
  <div class="abs field" style="top:2870px">Email</div>
  <div class="abs field" style="top:2910px;height:52px">Message</div>
  <div class="abs submit">Submit →</div>

  <div class="abs foot-h" style="left:852px">Follow Us</div>
  <div class="abs foot-rule" style="left:852px"></div>
  <div class="abs social foot-social"><span></span><span></span><span></span><span></span></div>
  <div class="abs foot-brand">PVT Law Group PLLC</div>

  <div class="abs copyright">Copyright © 2017 PVT Law Group pllc. All Rights Reserved.</div>
</div>
</body>
</html>
```